Website Design for Business Law Firm

We have a logo and now we would like a web site design for our new website. Our small firm provides creative and aggressive transactional (not litigation) legal services to advise healthcare, technology, internet-based and traditional companies and investors in such companies on healthcare, technology, financing, mergers/acquisitions, real estate and other transactions, legal compliance and general corporate and business matters.

We would like to see a website design that is professional and appropriate for executives, professionals, investors and government regulators to visit, that conveys professionalism and competence while being a little edgy and modern - no typical legal motifs such as gavels, books, or scales of justice. We advise businesses and investors and guide them through complicated issues quickly, capably and differently from other law firms. We are part of the business team and get things done.

The logo is attached, and we like gray as a color to complement it. The intention of the logo is to convey that in a storm or challenging time, people come to this firm, and people come to this firm when they need the power and disruption to change things or shake them up.

I have also enclosed a picture of our business card for consideration.

On the other hand, you can check out the current simple site at www.venhollow.example to see we have used a space motif in the past to evoke that we help create stars (the nebula featured there). This is not a necessary part of the new website and it may look better without it.

We appreciate your creativity and look forward to designs.

Industry/Entity Type

Business

Requirements
Must have
• We anticipate the following pages, and you may submit different ideas for the different pages:
• 1. Landing page
• 2. Services pages - healthcare, IT/Technology, general counsel services, financings, mergers/acquisitions, mediation/arbitration, procurement and productization
• 3. About Us including contact information
• Our name and contact information:
• Quellane Law Firm, P.C.
• 8716 SW 19th Ave.
• Portland, OR 97213
• phone: 971.555.0143
• fax: 971.555.0187
Nice to have
• Please consider designs that enhance the impressions we are looking for
Should not have
• Please no gavels, scales of justice, law books, or similar traditional legal imagery.

```html
<!DOCTYPE html>
<html lang="en">
<head>
<meta charset="utf-8">
<title>Quellane Law Firm — Practice Areas</title>
<link href="https://fonts.googleapis.com/css2?family=Cabin+Condensed:wght@400;500&display=swap" rel="stylesheet">
<style>
  :root {
    --band-gray: #5b5c5f;
    --band-gray-dark: #505154;
    --text-light: #ffffff;
    --accent-teal: #8ec7ca;
    --panel-shade: rgba(62, 60, 48, 0.62);
    --logo-box: #2c3036;
  }
  * { margin: 0; padding: 0; box-sizing: border-box; }
  html, body { width: 1200px; height: 1000px; overflow: hidden; }
  body {
    position: relative;
    font-family: "Cabin Condensed", "Arial Narrow", sans-serif;
    color: var(--text-light);
    background: var(--band-gray);
  }
  .site-header {
    position: absolute; left: 0; top: 0; width: 1200px; height: 146px;
    background: linear-gradient(180deg, var(--band-gray) 0%, var(--band-gray-dark) 100%);
  }
  .brand {
    position: absolute; left: 93px; top: 28px; width: 282px;
  }
  .brand-mark {
    display: flex; align-items: center; gap: 14px;
    height: 72px; padding: 0 14px;
    background: var(--logo-box);
    border-bottom: 2px solid #d8dde2;
  }
  .brand-square { width: 22px; height: 22px; background: var(--accent-teal); flex: none; }
  .brand-name {
    font-size: 40px; font-weight: 400; letter-spacing: 6px; color: var(--text-light);
  }
  .brand-tagline {
    margin-top: 8px; font-size: 14px; font-style: italic; color: var(--text-light);
    white-space: nowrap;
  }
  .main-nav { position: absolute; top: 64px; left: 0; width: 1200px; }
  .main-nav a {
    position: absolute; transform: translateX(-50%);
    font-size: 19px; color: var(--text-light); text-decoration: none; white-space: nowrap;
  }
  .hero {
    position: absolute; left: 0; top: 146px; width: 1200px; height: 757px;
  }
  .hero-photo {
    position: absolute; inset: 0;
    background:
      radial-gradient(ellipse 520px 200px at 1000px 120px, rgba(250,240,200,0.85), rgba(250,240,200,0) 70%),
      linear-gradient(180deg, #c9c08f 0%, #a69c6a 22%, #8b7b4c 45%, #8a6a3a 65%, #6e4d2a 85%, #4e3620 100%);
  }
  .services-panel {
    position: absolute; left: 229px; top: 146px; width: 731px; height: 421px;
    background: var(--panel-shade);
  }
  .services-title {
    position: absolute; left: 53px; top: 52px;
    font-size: 43px; font-weight: 500; font-style: italic; color: var(--accent-teal);
    white-space: nowrap;
  }
  .services-list {
    position: absolute; top: 145px; list-style: none;
    font-size: 19px; line-height: 23.5px; white-space: nowrap;
  }
  .services-list.left { left: 53px; }
  .services-list.right { left: 463px; }
  .site-footer {
    position: absolute; left: 0; top: 903px; width: 1200px; height: 97px;
    background: var(--band-gray);
    text-align: center; font-size: 18px; line-height: 23px; padding-top: 22px;
  }
</style>
</head>
<body>
  <header class="site-header">
    <div class="brand">
      <div class="brand-mark">
        <span class="brand-square"></span>
        <span class="brand-name">QUELLANE</span>
      </div>
      <p class="brand-tagline">Pragmatic, Creative Services for Innovative Businesses</p>
    </div>
    <nav class="main-nav">
      <a href="#" style="left:448px">Home</a>
      <a href="#" style="left:594px">About QUELLANE</a>
      <a href="#" style="left:740px">Practice Areas</a>
      <a href="#" style="left:886px">FAQs</a>
      <a href="#" style="left:1033px">Contact</a>
    </nav>
  </header>

  <section class="hero">
    <div class="hero-photo" role="img" aria-label="Aerial photograph of a city skyline under amber storm clouds at dusk"></div>
    <div class="services-panel">
      <h1 class="services-title">.Legal Services We Provide</h1>
      <ul class="services-list left">
        <li>Vendor Management</li>
        <li>Service as a Mediator or Aarbitrator</li>
        <li>Procurements-Buying or Selling</li>
        <li>Local Counsel for Transactions and Due Dilligence</li>
        <li>Licensing and Technology Exploitation</li>
        <li>Venture Formation and Startup</li>
        <li>Creative Private Financing Arrangements</li>
        <li>Audits, Analyses and Legal Project Management</li>
      </ul>
      <ul class="services-list right">
        <li>Strategic Alliances</li>
        <li>Business Relationships</li>
        <li>Outsourcing</li>
        <li>Dispute Resolution</li>
        <li>Venture Financing</li>
        <li>Mergers and Acquistions</li>
        <li>Real Estate</li>
        <li>Contracts</li>
      </ul>
    </div>
  </section>

  <footer class="site-footer">
    <p>Quellane Law Firm, P.C., P,.O. Box 6208, Portland, OR 97299</p>
    <p>info@quellane.example | 971.555.0143 phone | 971.555.0187 fax</p>
  </footer>
</body>
</html>
```